Gus Parnaby's Swingfold Big Band — Slick & Steady ------ CD Cover Art (and Disc Art)

Need a front cover jacket and a disc design for a fantastic all-pro big band (jazz/funk/reggae) CD. We really want to use a group photo somehow since so many of the band members are world famous, LA's finest studio musicians with mostly original music arranged by the biggest names in jazz. Playful, fun, lighthearted, tasteful arrangements with world class soloists.

Target Market(s)

Music/Jazz/Big band enthusiasts; other musicians

Font styles to use
Other font styles liked:
• See uploaded file #4

Colors

Designer to choose colors to be used in the design.

Requirements
Must have
• Legibility . . . must be easy to read and not crowded or cluttered. Font idea below (Three Lanterns Beneath The Quiet Tide) is for feel and flavor. It is absolutely not necessary to match if you have something you like better.
Nice to have
• Colorful but not tacky. Maybe a play on the CD title, Slick and Steady?

```html
<!DOCTYPE html>
<html lang="en">
<head>
<meta charset="utf-8">
<title>Gus Parnaby's Swingfold Big Band — Slick &amp; Steady</title>
<link rel="stylesheet" href="https://fonts.googleapis.com/css2?family=Rye&family=Oswald:wght@500&display=swap">
<style>
  :root{
    --ink:#26252a;
    --peach:#c8896a;
    --brick:#9b2a2e;
    --teal:#4b7f8e;
    --slate:#3d4a55;
    --sage:#5e8379;
    --coral:#e06468;
    --umber:#7d6a4b;
    --rose:#e46169;
    --cream:#f3ece0;
    --bronze:#8a6a45;
  }
  html,body{margin:0;padding:0;overflow:hidden;background:var(--ink);}
  .cover{position:relative;width:1200px;height:1200px;overflow:hidden;background:var(--ink);}
  .tile{position:absolute;}
  .photo{background:linear-gradient(160deg,#8a4b5a 0%,#b86e63 35%,#caa089 60%,#3b2d33 100%);}
  .photo.cool{background:linear-gradient(160deg,#2f7f86 0%,#4a6e5a 40%,#caa089 65%,#2a2a2e 100%);}
  .photo.green{background:linear-gradient(160deg,#4c6b3d 0%,#6f7f50 40%,#cfa38a 65%,#2b2b2e 100%);}
  .block-peach{background:var(--peach);}
  .block-brick{background:var(--brick);}
  .block-teal{background:var(--teal);}
  .block-slate{background:var(--slate);}
  .art-sax{background:linear-gradient(135deg,var(--sage),#7fa198);}
  .art-bass{background:linear-gradient(135deg,var(--coral),#f08a85);}
  .art-trumpet{background:linear-gradient(135deg,var(--umber),#9a8664);}

  .band-tag{position:absolute;left:55px;top:645px;width:558px;height:48px;background:var(--peach);
    display:flex;align-items:center;justify-content:center;overflow:hidden;
    font-family:"Rye",serif;font-size:22px;color:#2b2326;letter-spacing:0;white-space:nowrap;}
  .album-title{position:absolute;left:52px;top:722px;margin:0;
    font-family:"Rye",serif;font-weight:400;font-size:240px;line-height:205px;letter-spacing:-4px;
    transform:scaleX(0.6);transform-origin:left top;
    text-shadow:7px 5px 0 var(--cream);}
  .album-title .line{display:block;white-space:nowrap;}
  .c-red{color:var(--brick);} .c-teal{color:var(--teal);} .c-rose{color:var(--rose);}
  .c-peach{color:var(--peach);} .c-bronze{color:var(--bronze);} .c-brown{color:#6e5a3c;}

  .label-mark{position:absolute;left:877px;top:988px;width:323px;height:212px;background:var(--slate);
    display:flex;flex-direction:column;align-items:center;justify-content:center;
    font-family:"Oswald",sans-serif;font-weight:500;color:#ffffff;line-height:1.05;}
  .label-mark .name{font-size:40px;letter-spacing:1px;}
  .label-mark .sub{font-size:34px;letter-spacing:2px;}
</style>
</head>
<body>
<main class="cover">
  <div class="tile photo" style="left:0;top:0;width:205px;height:213px" role="img" aria-label="Band member portrait with saxophone"></div>
  <div class="tile photo cool" style="left:215px;top:0;width:140px;height:185px" role="img" aria-label="Band member portrait"></div>
  <div class="tile photo" style="left:365px;top:0;width:240px;height:238px" role="img" aria-label="Band member portrait playing saxophone"></div>
  <div class="tile art-sax" style="left:615px;top:0;width:280px;height:235px" role="img" aria-label="Line drawing of a saxophone"></div>
  <div class="tile photo green" style="left:908px;top:0;width:292px;height:152px" role="img" aria-label="Three band members together"></div>

  <div class="tile photo green" style="left:0;top:225px;width:205px;height:170px" role="img" aria-label="Band member portrait"></div>
  <div class="tile block-peach" style="left:215px;top:197px;width:140px;height:200px"></div>
  <div class="tile photo" style="left:365px;top:250px;width:148px;height:145px" role="img" aria-label="Band member portrait"></div>
  <div class="tile photo" style="left:523px;top:250px;width:215px;height:140px" role="img" aria-label="Two band members"></div>
  <div class="tile block-brick" style="left:750px;top:250px;width:145px;height:145px"></div>
  <div class="tile photo" style="left:908px;top:163px;width:137px;height:193px" role="img" aria-label="Guitarist portrait"></div>
  <div class="tile block-teal" style="left:1057px;top:163px;width:143px;height:390px"></div>

  <div class="tile photo green" style="left:0;top:405px;width:198px;height:148px" role="img" aria-label="Two band members with trombone"></div>
  <div class="tile art-bass" style="left:215px;top:407px;width:298px;height:146px" role="img" aria-label="Line drawing of an electric bass"></div>
  <div class="tile block-slate" style="left:523px;top:407px;width:147px;height:146px"></div>
  <div class="tile photo" style="left:682px;top:407px;width:215px;height:146px" role="img" aria-label="Two band members"></div>
  <div class="tile photo" style="left:908px;top:372px;width:137px;height:181px" role="img" aria-label="Band member portrait"></div>

  <div class="tile photo cool" style="left:684px;top:567px;width:145px;height:218px" role="img" aria-label="Trombonist in a ball cap"></div>
  <div class="tile photo" style="left:840px;top:567px;width:180px;height:218px" role="img" aria-label="Two band members"></div>
  <div class="tile photo" style="left:1030px;top:567px;width:170px;height:218px" role="img" aria-label="Band member with trumpet"></div>
  <div class="tile art-trumpet" style="left:682px;top:798px;width:320px;height:182px" role="img" aria-label="Line drawing of a trumpet"></div>
  <div class="tile photo" style="left:1012px;top:798px;width:188px;height:180px" role="img" aria-label="Band member portrait"></div>
  <div class="tile photo" style="left:682px;top:992px;width:185px;height:208px" role="img" aria-label="Band member portrait"></div>

  <div class="band-tag">GUS PARNABY'S SWINGFOLD BIG BAND</div>
  <h1 class="album-title">
    <span class="line"><span class="c-red">S</span><span class="c-bronze">L</span><span class="c-rose">I</span><span class="c-teal">C</span><span class="c-red">K</span> <span class="c-peach">&amp;</span></span>
    <span class="line"><span class="c-rose">S</span><span class="c-teal">T</span><span class="c-peach">E</span><span class="c-red">A</span><span class="c-brown">D</span><span class="c-teal">Y</span></span>
  </h1>

  <div class="label-mark">
    <span class="name">TALL FERN</span>
    <span class="sub">RECORDS</span>
  </div>
</main>
</body>
</html>
```